Environmental Plastics Infographic on Marine Debris

We need a series of infographics that can be used individually or as a combined presentation. We'd like the combined piece to include an introduction and conclusion along with 4-5 infographics. Each infographic (information unit) should also work as a standalone. We are trying to help people visualize size proportions and ratios to put the plastics marine debris problem in perspective. Our key point is concerning polystyrene foam which represents 35 tons. We are looking for something creative to help people understand what the problem represents in terms they are familiar with.

To view our typical company design/style please see our website at www.brantleyfoamworks.org. Our primary RGB colors are: (187,140,9); (94,47,29); (94,138,164); and (164,167,15). Secondary RGB colors are (249,162,28) and (218,210,208). Our title/header font is DIN Next LT Pro and our copy font is Calibri 10.5 pt. We can deviate from the font specification if beneficial and welcome interesting text treatments and typography.

Need extra days to review

Target Market(s)

international brand manufacturers (corvantel, makiro), US legislators & government agencies

Font styles to use
Sans Serif

Requirements
Must have
• Sufficient white space. Easy to grasp message concept with visual components.

```html
<!DOCTYPE html>
<html lang="en">
<head>
<meta charset="utf-8">
<title>How Will Polystyrene Bans Improve Ocean Health?</title>
<link rel="stylesheet" href="https://fonts.googleapis.com/css2?family=Barlow+Condensed:wght@600;700;800&family=Barlow+Semi+Condensed:wght@600;700&family=Barlow:wght@700;800&family=Carlito:wght@400;700&display=swap">
<style>
  :root{
    --gold:#b98c2c;
    --gold-dark:#a27826;
    --brown:#5e2f1d;
    --brown-soft:#74441f;
    --blue:#5e8aa4;
    --olive:#a4a70f;
    --olive-panel:#a2a638;
    --orange:#f9a21c;
    --stone:#dad2d0;
    --cream:#ecdcb0;
    --white:#ffffff;
    --head:"Barlow Semi Condensed", "Barlow", sans-serif;
    --cond:"Barlow Condensed", sans-serif;
    --copy:"Carlito", "Calibri", sans-serif;
  }
  *{box-sizing:border-box;margin:0;padding:0}
  html,body{width:1200px;height:1200px;overflow:hidden;background:var(--white)}
  body{position:relative;font-family:var(--copy)}
  .panel{position:absolute;overflow:hidden}
  .abs{position:absolute}
  .ph{position:absolute}

  /* Intro */
  .intro{left:151px;top:16px;width:900px;height:284px;background:var(--gold)}
  .intro-title{left:0;width:900px;top:12px;text-align:center;font:700 35px/1 var(--head);color:var(--brown);letter-spacing:.2px}
  .intro-copy{left:29px;top:56px;width:415px;font:700 14.6px/20.8px var(--copy);color:var(--white)}
  .intro-rule{left:448px;top:53px;width:3px;height:231px;background:var(--white)}
  .intro-side{left:462px;top:56px;width:420px;color:var(--brown);font:400 14.6px/18.5px var(--copy)}
  .intro-side .claim{text-align:center;font:600 16px/20.5px var(--head);color:var(--cream)}
  .intro-side .look{text-align:center;font:600 17px/1 var(--head);color:var(--orange);margin-top:12px}
  .intro-side .total{text-align:center;font:700 14.5px/1 var(--copy);color:var(--cream);margin-top:5px}
  .intro-side ul{list-style:none;margin-top:12px}
  .intro-side li{margin-left:10px;margin-bottom:7px}
  .intro-side li::before{content:"";display:inline-block;width:10px;height:10px;border-radius:50%;background:var(--orange);margin-right:7px;vertical-align:-1px}

  /* Compare columns */
  .compare{left:153px;top:314px;width:441px;height:284px;background:var(--orange)}
  .bigword{position:absolute;font:800 100px/1 var(--cond);color:var(--stone);letter-spacing:-1px}
  .col{position:absolute;width:99px;background:var(--blue);color:var(--stone);text-align:center}
  .col .lbl{font:700 14px/18px var(--head);padding-top:8px}
  .col .pct{position:absolute;bottom:4px;left:0;width:100%;font:700 15.5px/1 var(--head)}

  /* Weights table */
  .weights{left:609px;top:314px;width:441px;height:284px;background:var(--brown)}
  .weights-title{left:14px;top:6px;font:800 47px/1 var(--head);color:var(--olive);letter-spacing:3.4px}
  .wrow{position:absolute;left:17px;width:405px;height:50px}
  .wrow .item{position:absolute;left:90px;width:85px;height:100%;background:var(--olive);color:var(--brown);font:400 14px/14.5px var(--copy);display:flex;align-items:center;justify-content:center;text-align:center}
  .wrow .val{position:absolute;left:179px;width:226px;height:100%;background:var(--olive);color:var(--brown);font:400 14.5px/1 var(--copy);display:flex;align-items:center;padding-left:6px;gap:6px}
  .wrow .val svg{flex:none}

  /* Cars */
  .cars{left:151px;top:611px;width:441px;height:284px;background:var(--olive-panel)}
  .clip{left:18px;top:48px;width:186px;height:208px;background:var(--white);transform:rotate(-1.5deg);box-shadow:2px 3px 5px rgba(0,0,0,.35)}
  .clip-mast{left:8px;top:10px;display:flex;align-items:center;gap:5px;font:700 14px/1 var(--copy);color:#c0282e}
  .clip-mast .dot{width:16px;height:16px;border-radius:50%;background:#111}
  .clip-headline{left:8px;top:136px;width:172px;font:700 12px/12.7px "Carlito",serif;color:#222}
  .clip-meta{left:5px;top:188px;font:400 3.6px/1 var(--copy);color:#555}
  .cars-word{position:absolute;font:800 35px/27px var(--cond);text-transform:uppercase}

  /* Sizing */
  .sizing{left:609px;top:611px;width:441px;height:286px;background:var(--gold)}
  .sizing-title{left:0;width:441px;top:17px;text-align:center;font:700 40px/1 var(--head);color:var(--brown)}
  .stable{position:absolute;left:33px;top:60px;border-collapse:separate;border-spacing:2px 0;font:400 14px/1 var(--copy)}
  .stable th{background:var(--brown);color:var(--stone);font-weight:400;text-align:left;padding:0 0 0 15px;height:53px;line-height:17px}
  .stable td{height:24px;padding-left:15px;color:var(--brown);font-weight:700}
  .stable tr.shade td{background:var(--gold-dark);color:#caa35a;font-weight:400}
  .stable tr.first td{border-top:9px solid var(--gold)}
  .sizing-note{left:0;top:219px;width:441px;height:67px;background:var(--brown)}

  /* EPS */
  .eps{left:151px;top:911px;width:441px;height:285px;background:var(--brown)}
  .eps-title{right:27px;top:18px;text-align:right;font:700 30px/1 var(--head);color:var(--gold)}
  .eps-sub{right:28px;top:48px;text-align:right;font:700 28px/1 var(--head);color:var(--olive)}
  .erow{position:absolute;left:24px;width:389px;height:22px;color:var(--olive);font:400 14px/1 var(--copy);display:flex;align-items:center}
  .erow.shade{background:var(--brown-soft)}
  .erow .n{width:142px;padding-left:9px;font-weight:700}
  .erow .t{flex:1}

  /* Discoveries */
  .disc{left:610px;top:911px;width:440px;height:285px;background:var(--olive-panel)}
  .disc-title{left:23px;top:9px;font:800 30px/1 var(--head);color:var(--stone);letter-spacing:2.6px}
  .disc-list{left:0;top:42px;width:440px;height:104px;background:var(--stone);padding:6px 0 0 22px;color:var(--brown);font:700 15px/18.5px var(--copy);list-style:none}
  .disc-list li{margin-bottom:2px}
  .disc-list li::before{content:"";display:inline-block;width:10px;height:10px;border-radius:50%;background:var(--olive-panel);margin-right:7px;margin-left:2px;vertical-align:0}
  .disc-head{left:26px;top:153px;font:700 23px/1 var(--head);color:var(--brown)}
  .disc-body{left:26px;top:177px;width:400px;font:400 14px/16.4px var(--copy);color:var(--brown)}
  .disc-src{left:23px;top:259px;font:400 9.4px/1 var(--copy);color:var(--brown)}
</style>
</head>
<body>

<section class="panel intro">
  <h1 class="abs intro-title">HOW WILL POLYSTYRENE BANS IMPROVE OCEAN HEALTH?</h1>
  <p class="abs intro-copy">A recent report looks at the role plastics play in marine debris that sheds light on previous assumptions about how different plastics contribute to the problem and where its coming from. In this ground breaking study, scientists conducted cutting-edge research at a much larger scale than had ever been done before. Over the course of three years, an international team including The Tidewater Cleanup Foundation, six universities, and an aerial sensor company, collected data and mapped debris fields for the Great Pacific Garbage Patch, one of the most problematic plastic pollution hot spots.</p>
  <div class="abs intro-rule"></div>
  <div class="abs intro-side">
    <p class="claim">POLYSTYRENE BAN LEGISLATION IMPLY PRODUCT RESTRICTIONS WILL MINIMIZE PLASTIC MARINE DEBRIS.</p>
    <p class="look">LET’S TAKE A CLOSER LOOK.</p>
    <p class="total">The Total Plastics Mass In The Gpgp Is Projected At 78,908 Tons.</p>
    <ul>
      <li>52% is mostly abandoned fishing gear, not consumer plastics.</li>
      <li>47% is hard plastics, sheets and film, making up the majority of the microplastics mass.</li>
      <li>0.05% is foamed plastics – including polystyrene – making it a minor component of the GPGP</li>
    </ul>
  </div>
</section>

<section class="panel compare">
  <span class="bigword" style="left:17px;top:18px;font-size:96px;letter-spacing:2px">HOW</span>
  <span class="bigword" style="left:17px;top:98px;font-size:62px">BIG</span>
  <span class="bigword" style="left:17px;top:156px;font-size:58px">IS</span>
  <span class="bigword" style="left:17px;top:208px;font-size:60px">BIG</span>
  <span class="bigword" style="left:72px;top:148px;font-size:138px">?</span>

  <div class="col" style="left:126px;top:98px;height:168px">
    <div class="lbl">1 Cruise Ship<br>100,000 tons</div>
    <div class="ph" role="img" aria-label="Photo of a cruise ship at sea" style="left:0;top:55px;width:99px;height:78px;background:linear-gradient(#c8d8e6,#e8eef3 45%,#2f5d86 70%,#1f4a73)"></div>
    <div class="pct">GPGP = 79%</div>
  </div>
  <div class="col" style="left:230px;top:65px;height:201px">
    <div class="lbl">1 Blue Whale<br>150,000 tons</div>
    <div class="ph" role="img" aria-label="Photo of a blue whale underwater" style="left:0;top:88px;width:99px;height:78px;background:linear-gradient(#1d6fb0,#0f5796 60%,#0a3f74)"></div>
    <div class="pct">GPGP = 53%</div>
  </div>
  <div class="col" style="left:334px;top:20px;height:246px">
    <div class="lbl">1 Week<br>NYC Waste<br>Generation<br>269,230 tons</div>
    <div class="ph" role="img" aria-label="Illustration of the New York skyline with a garbage truck" style="left:0;top:133px;width:99px;height:79px;background:linear-gradient(var(--blue),#8a9a5a 60%,#c98a3a)"></div>
    <div class="pct">GPGP = 29%</div>
  </div>
</section>

<svg width="0" height="0" style="position:absolute" aria-hidden="true">
  <defs>
    <symbol id="weight" viewBox="0 0 26 26">
      <circle cx="13" cy="5" r="3.6" fill="none" stroke="#c9c9c9" stroke-width="2.2"/>
      <path d="M7 9 H19 L24 25 H2 Z" fill="#c4c4c4" stroke="#9a9a9a" stroke-width=".6"/>
      <text x="13" y="21" text-anchor="middle" font-family="Carlito, sans-serif" font-size="6.5" fill="#555">50K</text>
    </symbol>
    <symbol id="weight-sm" viewBox="0 0 26 26">
      <circle cx="13" cy="5" r="3.6" fill="none" stroke="#c9c9c9" stroke-width="2.2"/>
      <path d="M7 9 H19 L24 25 H2 Z" fill="#c4c4c4" stroke="#9a9a9a" stroke-width=".6"/>
    </symbol>
  </defs>
</svg>

<section class="panel weights">
  <h2 class="abs weights-title">HOW BIG IS BIG?</h2>
  <div class="wrow" style="top:53px">
    <div class="ph" role="img" aria-label="Photo of plastic debris floating in the ocean" style="left:0;top:0;width:88px;height:50px;background:linear-gradient(135deg,#1e6a6e,#4d9a92 50%,#2d5f5a)"></div>
    <div class="item">All GPGP<br>Plastics</div>
    <div class="val">78,908 tons <svg width="26" height="26"><use href="#weight"/></svg><svg width="20" height="20"><use href="#weight-sm"/></svg></div>
  </div>
  <div class="wrow" style="top:110px">
    <div class="ph" role="img" aria-label="Photo of a cruise ship" style="left:0;top:0;width:88px;height:50px;background:linear-gradient(#c8d8e6,#e8eef3 45%,#2f5d86 72%)"></div>
    <div class="item">1 Cruise<br>Ship</div>
    <div class="val">100,000 tons <svg width="26" height="26"><use href="#weight"/></svg><svg width="26" height="26"><use href="#weight"/></svg></div>
  </div>
  <div class="wrow" style="top:165px">
    <div class="ph" role="img" aria-label="Photo of a blue whale" style="left:0;top:0;width:88px;height:50px;background:linear-gradient(#1d6fb0,#0a3f74)"></div>
    <div class="item">1 Blue<br>Whale</div>
    <div class="val">150,000 tons <svg width="26" height="26"><use href="#weight"/></svg><svg width="26" height="26"><use href="#weight"/></svg><svg width="26" height="26"><use href="#weight"/></svg></div>
  </div>
  <div class="wrow" style="top:222px">
    <div class="ph" role="img" aria-label="Illustration of the New York skyline with a garbage truck" style="left:8px;top:8px;width:72px;height:42px;background:linear-gradient(var(--brown),#8a8a3a 55%,#c98a3a)"></div>
    <div class="item" style="background:var(--olive)">1 Week<br>NYC Waste<br>Generation</div>
    <div class="val">269,230 tons <svg width="26" height="26"><use href="#weight"/></svg><svg width="26" height="26"><use href="#weight"/></svg><svg width="26" height="26"><use href="#weight"/></svg><svg width="26" height="26"><use href="#weight"/></svg><svg width="14" height="14"><use href="#weight-sm"/></svg></div>
  </div>
</section>

<section class="panel cars">
  <svg class="abs" style="left:0;top:0" width="441" height="284" aria-hidden="true">
    <circle cx="304" cy="62" r="22" fill="#b7b96a"/>
    <circle cx="190" cy="210" r="72" fill="none" stroke="#b8bb66" stroke-width="14" opacity=".6"/>
  </svg>
  <div class="abs clip">
    <div class="abs clip-mast"><span class="dot"></span>Civic Evening News</div>
    <div class="ph" role="img" aria-label="Photo of researchers on a sailboat deck with sampling nets over the ocean" style="left:8px;top:32px;width:168px;height:88px;background:linear-gradient(#8fb6cf,#2f5f8c 45%,#1d3f66)"></div>
    <p class="abs clip-headline">Great Pacific Garbage Patch weighs more than 43,000 cars and is much larger than we thought</p>
    <p class="abs clip-meta">Science · Mar 22, 2018 · Updated Apr 18, 2018</p>
  </div>
  <div class="cars-word" style="left:210px;top:43px;color:var(--white);font-size:34px">TOTAL</div>
  <div class="cars-word" style="left:210px;top:68px;color:var(--brown);font-size:38px">GPGP</div>
  <div class="cars-word" style="left:210px;top:97px;color:var(--white);font-size:35px">MASS</div>
  <div class="cars-word" style="left:300px;top:60px;color:var(--brown);font-size:62px;line-height:44px">&gt;</div>
  <div class="cars-word" style="left:343px;top:54px;color:var(--brown);font-size:33px;line-height:36px">43,000<br>CARS</div>
  <div class="cars-word" style="left:207px;top:151px;color:var(--brown);font-size:40px;line-height:32px">TOTAL FOAM</div>
  <div class="cars-word" style="left:209px;top:191px;color:var(--white);font-size:34px">PLASTIC MASS</div>
  <div class="cars-word" style="left:207px;top:220px;color:var(--white);font-size:62px;line-height:50px">18 CARS</div>
</section>

<section class="panel sizing">
  <h2 class="abs sizing-title">SIZING IT UP</h2>
  <table class="stable">
    <tr><th style="width:106px">Total GPGP<br>78.9 K Tons</th><th style="width:134px">Marine Debris<br>Size Classes</th><th style="width:126px">Measurement<br>Values</th></tr>
    <tr class="shade first"><td>42 tons</td><td>Megaplastics</td><td>&gt;50 cm</td></tr>
    <tr><td>10 tons</td><td>Macroplastics</td><td>5 – 50 cm</td></tr>
    <tr class="shade"><td>20 tons</td><td>Mesoplastics</td><td>0.5 – 5 cm</td></tr>
    <tr><td>6.5 tons</td><td>Microplastics</td><td>0.05 – 0.5 cm</td></tr>
  </table>
  <div class="abs sizing-note">
    <p class="abs" style="left:49px;top:6px;font:700 14.5px/18px var(--copy);color:var(--olive)">Mesoplastics<br><span style="font-weight:400;color:var(--cream)">Think peppercorn to house key.</span></p>
    <div class="ph" role="img" aria-label="Photo of a peppercorn" style="left:266px;top:25px;width:10px;height:10px;border-radius:50%;background:radial-gradient(#6a5a3a,#2a2418)"></div>
    <div class="ph" role="img" aria-label="Photo of a house key" style="left:294px;top:8px;width:76px;height:44px;background:linear-gradient(160deg,#e4dcc8,#a89e88)"></div>
  </div>
</section>

<section class="panel eps">
  <h2 class="abs eps-title">HOW MUCH MISMANAGED EPS</h2>
  <h3 class="abs eps-sub">Waste Was Found?</h3>
  <div class="erow shade" style="top:89px"><span class="n">320,000,000 tons</span><span class="t">Worldwide Annual Plastics Production</span></div>
  <div class="erow" style="top:111px"><span class="n">78,908 tons</span><span class="t">Total GPGP Plastics</span></div>
  <div class="erow shade" style="top:134px"><span class="n">0.000024%</span><span class="t">Percent of Global Production in GPGP</span></div>
  <div class="erow shade" style="top:178px;height:42px;align-items:flex-start;padding-top:5px"><span class="n">6,620,000 tons</span><span class="t" style="line-height:17px">Worldwide Expanded Polystyrene<br>(EPS) Plastics Production</span></div>
  <div class="erow" style="top:223px"><span class="n">35 tons</span><span class="t">Total GPGP Foam Plastics</span></div>
  <div class="erow shade" style="top:246px"><span class="n">0.0000053%</span><span class="t">Percent of Global Production in GPGP</span></div>
</section>

<section class="panel disc">
  <h2 class="abs disc-title">SURPRISING DISCOVERIES</h2>
  <ul class="abs disc-list">
    <li>Approximately 50% of GPGP Plastics are From Marine-Based Sources.</li>
    <li>Beach Litter Studies Were Not Indicative of GPGP Content.</li>
    <li>20% of the GPGP Plastic Debris Is From the 2011 Tohoku Tsunami</li>
  </ul>
  <h3 class="abs disc-head">All Marine Plastic Debris Is A Problem!</h3>
  <p class="abs disc-body">However, plastic product bans will be ineffective in reducing ocean debris.<br>Since the U.S. contributes just 0.9% of the World’s Mismanaged Plastic Waste¹, it is even more important to consider all parts of equation.</p>
  <p class="abs disc-src"><sup>1</sup>Source: 6 things you can do to stop plastic pollution today, Daily Ledger, September 7, 2018</p>
</section>

</body>
</html>
```